Author and Publisher

Cover for a book on the process of publishing a book from the presentation to the publisher until the selling in bookstores :
A behind-the-scenes journey through the world of book publishing, from manuscript to bookstore. The book explores the relationship between authors and publishers, manuscript selection, contracts, editing, proofreading, book design, printing, distribution, bookstores and online sales. It reveals the many people, decisions and processes involved in turning a text into a physical book and bringing it to readers. The illustration should evoke publishing as a lively, contemporary ecosystem, combining creativity, craftsmanship, business and the enduring appeal of books.
FORMAT : 14 x 20,5 cm
AUTHOR : Luc Varennes
TITLE : Le scribe et la presse
PUBLISHER : Editions Trovel (at the bottom of the page)
Target Market(s)
General public, mainly news authors of books
Look and feel
Each slider illustrates characteristics of the customer's brand and the style your logo design should communicate.

```html
<!DOCTYPE html>
<html lang="fr">
<head>
<meta charset="utf-8">
<title>Le scribe et la presse — Luc Varennes</title>
<link rel="stylesheet" href="https://fonts.googleapis.com/css2?family=Bebas+Neue&display=swap">
<style>
  :root {
    --backdrop: #808080;
    --cover: #30434e;
    --shelf: #c9983a;
    --ink: #2b2f38;
    --paper: #ffffff;
  }
  html, body {
    margin: 0;
    width: 1200px;
    height: 1199px;
    overflow: hidden;
    background: var(--backdrop);
  }
  .cover-art {
    display: block;
    width: 1200px;
    height: 1199px;
  }
  .cover-panel { fill: var(--cover); }
  .shelf-plank { fill: var(--shelf); }
  .title-line {
    font-family: "Bebas Neue", "Oswald", sans-serif;
    fill: var(--ink);
    font-size: 230px;
    letter-spacing: 6px;
    text-anchor: middle;
  }
  .title-joiner {
    font-family: "Bebas Neue", "Oswald", sans-serif;
    fill: var(--paper);
    font-size: 150px;
    text-anchor: middle;
  }
  .author-name {
    font-family: "Bebas Neue", "Oswald", sans-serif;
    fill: var(--paper);
    font-size: 92px;
    letter-spacing: 2px;
    text-anchor: middle;
  }
  .publisher-name {
    font-family: "Bebas Neue", "Oswald", sans-serif;
    fill: var(--shelf);
    font-size: 38px;
    letter-spacing: 4px;
    text-anchor: middle;
  }
</style>
</head>
<body>
<svg class="cover-art" viewBox="0 0 1500 1499" xmlns="http://www.w3.org/2000/svg" role="img" aria-label="Couverture : Le scribe et la presse, Luc Varennes, Editions Trovel">
  <defs>
    <linearGradient id="upper-shelf-tones" x1="0" y1="0" x2="1" y2="0">
      <stop offset="0" stop-color="#e8c35a"/>
      <stop offset="0.17" stop-color="#ffffcc"/>
      <stop offset="0.33" stop-color="#ff6600"/>
      <stop offset="0.5" stop-color="#00ccff"/>
      <stop offset="0.66" stop-color="#66ffcc"/>
      <stop offset="0.83" stop-color="#ff0000"/>
      <stop offset="1" stop-color="#ffcc00"/>
    </linearGradient>
    <linearGradient id="lower-shelf-tones" x1="0" y1="0" x2="1" y2="0">
      <stop offset="0" stop-color="#cc3300"/>
      <stop offset="0.15" stop-color="#9900cc"/>
      <stop offset="0.3" stop-color="#ffff00"/>
      <stop offset="0.45" stop-color="#ffcc99"/>
      <stop offset="0.6" stop-color="#ff6633"/>
      <stop offset="0.72" stop-color="#e8c35a"/>
      <stop offset="0.86" stop-color="#00ccff"/>
      <stop offset="1" stop-color="#99ff00"/>
    </linearGradient>
  </defs>

  <rect class="cover-panel" x="300" y="105" width="897" height="1285"/>

  <rect class="shelf-plank" x="300" y="105" width="897" height="32"/>

  <rect x="330" y="188" width="835" height="467" fill="url(#upper-shelf-tones)" opacity="0.9"
        role="img" aria-label="Rangée de livres colorés sur une étagère"/>

  <rect class="shelf-plank" x="300" y="655" width="897" height="33"/>

  <rect x="333" y="735" width="831" height="417" fill="url(#lower-shelf-tones)" opacity="0.9"
        role="img" aria-label="Seconde rangée de livres colorés, l'un penché"/>

  <rect class="shelf-plank" x="300" y="1152" width="897" height="33"/>

  <text class="title-line" x="748" y="500">LE SCRIBE</text>
  <text class="title-joiner" x="748" y="645">ET</text>
  <text class="title-line" x="748" y="1035">LA PRESSE</text>

  <text class="author-name" x="749" y="1320">LUC VARENNES</text>
  <text class="publisher-name" x="749" y="1372">EDITIONS TROVEL</text>
</svg>
</body>
</html>
```